Web Design Project - KornHaus.de

The page shall provide individual brown-bread mix.
There shall be presented:
* RECIPES: consumer's choice and feedback area
* EQUIPMENT: baking equipment store
* BREAD-MIX: individual mix and configurator function for bread-mix
The consumer can search/view the content and checkout the products. A user can establish a profile. A user can interact on the page for feedback on content and connection to social media.
Industry/Entity Type
Store
Look and feel
Each slider illustrates characteristics of the customer's brand and the style your logo design should communicate.

```html
<!DOCTYPE html>
<html lang="en">
<head>
<meta charset="utf-8">
<title>KornHaus.de – Bread Mix Store</title>
<link rel="stylesheet" href="https://fonts.googleapis.com/css2?family=Fira+Sans+Condensed:wght@400;600&family=PT+Sans:ital,wght@0,400;0,700;1,400;1,700&display=swap">
<style>
:root{
  --bg:#1a0d07;
  --cream:#f1e0cb;
  --tan:#c9a96e;
  --bar:#6b5034;
  --hero-text:#a07a52;
  --ink:#1a0d07;
  --light:#f5ece0;
  --heading-tan:#d8b88c;
  --blue-head:#5a8fd0;
  --teal-head:#3fa4b0;
  --gold-head:#e0a83a;
}
*{margin:0;padding:0;box-sizing:border-box}
html,body{width:1200px;height:1132px;overflow:hidden;background:var(--bg)}
body{position:relative;font-family:"PT Sans",sans-serif;color:var(--light)}
.abs{position:absolute}

.brand-mark{left:152px;top:18px;width:46px;height:58px;border-radius:12px;background:#9c8a78}
.brand-name{left:212px;top:36px;font-size:25px;font-weight:700;color:#fff;letter-spacing:.3px}

.search{left:942px;top:13px;width:116px;height:21px;background:#fff;border-radius:11px;color:#444;font-size:11px;padding:3px 0 0 10px}
.search svg{position:absolute;right:7px;top:4px}

.nav{right:143px;top:53px;display:flex;align-items:center;font-family:"Fira Sans Condensed",sans-serif;font-weight:600;font-size:12.5px}
.nav a{color:#fff;text-decoration:none;padding:2px 8px}
.nav span{color:#fff}
.nav a.current{background:var(--cream);color:var(--ink);padding:2px 10px}

.hero{left:141px;top:86px;width:916px;height:380px;background:#fff;border-radius:12px 12px 0 0;overflow:hidden}
.hero-photo{position:absolute;left:336px;top:0;width:580px;height:380px;background:radial-gradient(ellipse at 55% 60%,#a9825a 0%,#8c653f 45%,#c7ad8e 75%,#fff 100%)}
.hero-text{position:absolute;left:19px;top:104px;width:340px;font-size:27px;line-height:36.5px;font-style:italic;font-weight:700;color:var(--hero-text)}
.slider-bar{left:139px;top:447px;width:920px;height:36px;background:var(--bar);border-radius:0 0 12px 12px}
.dots{left:562px;top:458px;display:flex;gap:6px}
.dots i{display:block;width:14px;height:14px;border:2px solid #fff;border-radius:50%}

.card{top:540px;width:275px;height:145px;background:var(--cream);border:2px solid var(--tan);color:var(--ink);padding:5px 0 0 13px}
.card h2{font-size:19px;font-style:italic;font-weight:700;line-height:22px;margin-left:2px}
.card p{width:170px;font-size:10.4px;line-height:14.2px;font-style:italic;font-weight:700}
.card .pic{position:absolute;right:9px;top:21px;width:80px;height:95px}
.card .more{position:absolute;right:18px;bottom:3px;font-size:10.4px;font-style:italic;font-weight:700}

.divider{left:0;top:722px;width:1200px;height:2px;background:#2a170d}

.foot-col{font-family:"Fira Sans Condensed",sans-serif;font-weight:600}
.foot-h{font-size:18px;color:#fff}
.links{left:194px;top:746px}
.links .foot-h{color:var(--heading-tan);margin-left:2px;margin-bottom:4px}
.links li{list-style:none;font-size:13.5px;line-height:25.3px;color:#fff}
.links li::before{content:"→ ";}

.stats{left:380px;top:746px;width:152px}
.stats p{font-size:13.5px}
.stats .big{font-size:38px;line-height:40px}
.stats hr{border:0;border-top:1px dotted #5a4535;margin:10px 0 12px}
.plus-btn{width:58px;height:37px;background:#e9eef5;border-radius:3px;border-top:5px solid #c9c9c9;margin-top:8px}

.share{left:612px;top:746px}
.circles{position:relative;margin-top:14px;width:90px}
.circles i{position:absolute;width:36px;height:36px;border-radius:50%;border:2px solid #d8d8d8}

.talk{left:801px;top:746px;width:184px}
.field{width:184px;height:31px;background:var(--cream);color:#5a4535;font-size:13.5px;padding:7px 10px;margin-top:10px}
.field.msg{height:109px}
.submit{left:852px;top:1028px;width:131px;height:33px;background:#a98c5c;display:flex}
.submit b{flex:1;color:var(--ink);font-size:15px;text-align:center;line-height:33px;font-weight:600;font-family:"Fira Sans Condensed",sans-serif}
.submit span{width:24px;border-left:1px solid #7a6240;background:#8d7450;position:relative}
.submit span::after{content:"";position:absolute;left:8px;top:12px;border-left:7px solid #3a2a1a;border-top:5px solid transparent;border-bottom:5px solid transparent}

.legal{left:0;top:1096px;width:1200px;height:36px;background:var(--cream);color:var(--ink);font-size:11.5px}
.legal .l{position:absolute;left:143px;top:11px}
.legal .r{position:absolute;right:143px;top:11px}
</style>
</head>
<body>

<div class="abs brand-mark"></div>
<div class="abs brand-name">KORNHAUS.DE</div>

<div class="abs search">Search
  <svg width="18" height="12" viewBox="0 0 18 12"><circle cx="6" cy="6" r="5" fill="none" stroke="#777" stroke-width="1.3"/><line x1="10" y1="8" x2="16" y2="11" stroke="#777" stroke-width="1.6"/></svg>
</div>

<nav class="abs nav">
  <a class="current">Home</a><a>About Us</a><span>|</span><a>Recipes</a><span>|</span><a>Equipment</a><span>|</span><a>Bread-Mix</a><span>|</span><a>Contact Us</a>
</nav>

<section class="abs hero">
  <div class="hero-photo" role="img" aria-label="Sliced loaf of dark rye bread"></div>
  <p class="hero-text">Lorem Ipsum is simply dummy text of the printing and typesetting industry.</p>
</section>
<div class="abs slider-bar"></div>
<div class="abs dots"><i></i><i></i><i></i><i></i></div>

<article class="abs card" style="left:142px">
  <h2>Recipes</h2>
  <p>Lorem Ipsum is simply dummy text of the printing and typesetting industry. Lorem Ipsum has been the industry's standard dummy text ever since the 1500s, when an unknown printer took a galley of type and scrambled it to make a type specimen book.</p>
  <div class="pic" role="img" aria-label="Recipe notebook with kitchen utensils" style="background:#b08a5c"></div>
  <span class="more">+Read More</span>
</article>
<article class="abs card" style="left:463px">
  <h2>Equipment</h2>
  <p>Lorem Ipsum is simply dummy text of the printing and typesetting industry. Lorem Ipsum has been the industry's standard dummy text ever since the 1500s, when an unknown printer took a galley of type and scrambled it to make a type specimen book.</p>
  <div class="pic" role="img" aria-label="Baking tools, cutters and eggs" style="background:linear-gradient(135deg,#d9c7b0,#d98a4a)"></div>
  <span class="more">+Read More</span>
</article>
<article class="abs card" style="left:784px">
  <h2>Bread-Mix</h2>
  <p>Lorem Ipsum is simply dummy text of the printing and typesetting industry. Lorem Ipsum has been the industry's standard dummy text ever since the 1500s, when an unknown printer took a galley of type and scrambled it to make a type specimen book.</p>
  <div class="pic" role="img" aria-label="Round crusty bread loaf" style="background:radial-gradient(ellipse,#b98450,#e8dccd)"></div>
  <span class="more">+Read More</span>
</article>

<div class="abs divider"></div>

<div class="abs foot-col links">
  <div class="foot-h">Read More</div>
  <ul><li>About Us</li><li>Recipes</li><li>Equipment,</li><li>Bread-Mix</li><li>Contact Us</li></ul>
</div>

<div class="abs foot-col stats">
  <div class="foot-h"><span style="color:var(--blue-head)">Circlebook</span> Like:</div>
  <p style="margin-top:6px">We Have More than</p>
  <p class="big" style="margin-left:10px">1500+</p>
  <p>Fans and still counting</p>
  <hr>
  <div class="foot-h"><span style="color:var(--teal-head)">Chirper</span> Tweets:</div>
  <p style="margin-top:6px">Our Chirper Users has posted</p>
  <p><span class="big">500+</span> Tweets Daily</p>
  <hr>
  <div class="foot-h"><span style="color:var(--gold-head)">Searchly</span> +1:</div>
  <div class="plus-btn"></div>
</div>

<div class="abs foot-col share">
  <div class="foot-h">Share Now:</div>
  <div class="circles">
    <i style="left:-3px;top:0;background:#d9dde2"></i><i style="left:45px;top:0;background:#f07a1a"></i>
    <i style="left:-3px;top:41px;background:#3aa53a"></i><i style="left:45px;top:41px;background:#4aa6e0"></i>
    <i style="left:-3px;top:84px;background:#3aa53a"></i><i style="left:45px;top:84px;background:#6a6a6a"></i>
    <i style="left:-3px;top:128px;background:#e2e2e2"></i><i style="left:45px;top:128px;background:#f0f0f0"></i>
    <i style="left:-3px;top:171px;background:#2e6fa8"></i><i style="left:45px;top:171px;background:#c8ccd2"></i>
    <i style="left:-3px;top:214px;background:#e2e2e2"></i><i style="left:45px;top:214px;background:#6a2a9a"></i>
  </div>
</div>

<form class="abs foot-col talk">
  <div class="foot-h">Lets Talk:</div>
  <div class="field">Name...</div>
  <div class="field">Email...</div>
  <div class="field">Phone No.</div>
  <div class="field msg">Message...</div>
</form>
<div class="abs submit"><b>Submit</b><span></span></div>

<footer class="abs legal">
  <span class="l">Copyright©2011 KornHaus.de | All Rights Reserved</span>
  <span class="r">Home | About Us | Recipes | Equipment | Bread-Mix | Contact Us</span>
</footer>

</body>
</html>
```